Lumo Brew Premium Matcha brand Label

This is a label design project for a luxury tea brand. Feel free to be creative within the guidelines.
Attached to this project is a document called “Private Label Design Requirements” with the design guidelines and template. There is another document called "Lumo Brew Packaging Instructions" this has more details necessary to stick to the guidelines in the first document.

I have also attached the certifications to be included as well as different variations of the logo for you to use.

If you have any questions, I am here.
Updates

Target Market(s)

Young, active, fun, enjoy the finer things

```html
<!DOCTYPE html>
<html lang="en">
<head>
<meta charset="utf-8">
<title>Lumo Brew Premium Ceremonial Matcha – Label Set</title>
<link href="https://fonts.googleapis.com/css2?family=Open+Sans:wght@600;700;800&display=swap" rel="stylesheet">
<style>
  :root{
    --page:#d1d2d4;
    --label:#0d0d0d;
    --label-edge:#1a1a1a;
    --ink:#ffffff;
    --matcha:#5cb531;
    --badge-green:#3f8f3a;
    --badge-blue:#2d6fb0;
  }
  *{box-sizing:border-box;margin:0;padding:0}
  html,body{width:1200px;height:631px;overflow:hidden;background:var(--page)}
  body{position:relative;font-family:"Open Sans",Arial,sans-serif;color:var(--ink)}

  /* lid label */
  .lid-label{position:absolute;left:81px;top:203px;width:224px;height:224px;border-radius:50%;
    background:var(--label);box-shadow:4px 6px 10px rgba(0,0,0,.25);text-align:center}
  .lid-label .brand{position:absolute;top:52px;left:0;right:0}
  .lid-label .title{position:absolute;top:105px;left:0;right:0;font-weight:800;font-size:16px;line-height:17.5px;letter-spacing:.3px}
  .lid-label .frame{position:absolute;left:38px;top:113px;width:150px;height:54px}
  .lid-label .weight{position:absolute;top:184px;left:0;right:0;font-weight:700;font-size:15px}

  .brand{display:flex;align-items:center;justify-content:center;gap:6px;font-weight:700;font-size:13px;letter-spacing:.3px}
  .brand .dot{width:14px;height:14px;border-radius:50%;background:var(--matcha)}
  .accent{color:var(--matcha)}

  /* wrap label */
  .wrap-label{position:absolute;left:347px;top:240px;width:780px;height:151px;
    background:linear-gradient(115deg,var(--label) 0%,var(--label-edge) 45%,var(--label) 70%,#141414 100%);
    box-shadow:8px 10px 14px rgba(0,0,0,.35)}
  .origin{position:absolute;left:55px;top:80px;font-weight:700;font-size:7px;line-height:8.4px}
  .origin .cert{margin-top:4px}
  .wrap-label .brand{position:absolute;top:55px;left:0;right:0}
  .wrap-label .title{position:absolute;top:79px;left:0;right:0;text-align:center;font-weight:800;font-size:17px;line-height:18px;letter-spacing:.4px}
  .wrap-label .frame{position:absolute;left:266px;top:86px;width:248px;height:24px}
  .wrap-label .weight{position:absolute;top:122px;left:0;right:0;text-align:center;font-weight:700;font-size:12px}

  .facts{position:absolute;left:592px;top:33px;font-weight:700}
  .facts h3{font-size:8.5px;line-height:11px}
  .facts p,.facts li{font-size:5.5px;line-height:6.6px}
  .facts ul{list-style:none;margin-bottom:6px}
  .facts .lead{margin-bottom:3px}
  .marks{display:flex;align-items:center;gap:3px;font-size:5.5px;line-height:6.5px}
  .mark-square{width:25px;height:18px;background:var(--badge-blue);border:1.5px solid var(--badge-green)}
  .mark-circle{width:18px;height:18px;border-radius:50%;background:var(--badge-green);border:1.5px solid #fff;margin-right:3px}
</style>
</head>
<body>

<section class="lid-label" aria-label="Lid label">
  <div class="brand"><span class="dot"></span>Lumo Brew</div>
  <svg class="frame" viewBox="0 0 150 54" fill="none" stroke="#fff" stroke-width="1.6">
    <path d="M32 1H1V53H37"/><path d="M118 1H149V53H113"/>
  </svg>
  <div class="title">PREMIUM<br>ORGANIC<br>CEREMONIAL<br><span class="accent">MATCHA</span></div>
  <div class="weight">1oz</div>
</section>

<section class="wrap-label" aria-label="Jar wrap label">
  <div class="origin">
    <p>Product of Japan</p>
    <p>Distributed by:</p>
    <p>Lumo Brew Co. | Riverton, Ga</p>
    <p class="cert">Certified Organic by verdana cert</p>
  </div>

  <div class="brand"><span class="dot"></span>Lumo Brew</div>
  <svg class="frame" viewBox="0 0 248 24" fill="none" stroke="#fff" stroke-width="1.6">
    <path d="M36 1H1V23H22"/><path d="M212 1H247V23H226"/>
  </svg>
  <div class="title">PREMIUM ORGANIC<br>CEREMONIAL <span class="accent">MATCHA</span></div>
  <div class="weight">1oz</div>

  <div class="facts">
    <h3>Ingredients:</h3>
    <p class="lead">Premium Organic Japanese Matcha Green Tea</p>
    <h3>Instructions:</h3>
    <ul>
      <li>• 2 tsp of Matcha</li>
      <li>• 2oz of Water (170-180 degrees F)</li>
      <li>• Whisk in a W formation until frothy</li>
      <li>• Sweeten to taste</li>
    </ul>
    <div class="marks">
      <span class="mark-square" role="img" aria-label="Non-GMO certification badge"></span>
      <span class="mark-circle" role="img" aria-label="Organic certification seal"></span>
      <span>KEEP REFRIGERATED<br>FOR QUALITY</span>
    </div>
  </div>
</section>

</body>
</html>
```